Criação de Layout Web-Design para Planejamento de Eventos
A empresa queria:
" Trabalho com decoração de festas, criamos projetos exclusivos. o site é para mostrar como fica o projeto executado "

```html
<!DOCTYPE html>
<html lang="pt-BR">
<head>
<meta charset="utf-8">
<title>Lume Festas — Casamento Luísa e Marcos</title>
<link href="https://fonts.googleapis.com/css2?family=Oswald:wght@400;500&family=Open+Sans:wght@400;600&display=swap" rel="stylesheet">
<style>
  :root {
    --header: #6f6161;
    --header-text: #f3eded;
    --accent: #d9a6a6;
    --accent-dark: #c98f8f;
    --band: #ebe8e8;
    --title: #5f5252;
    --text: #7a7070;
    --page: #ffffff;
  }
  * { box-sizing: border-box; margin: 0; padding: 0; }
  html, body { width: 1200px; height: 1200px; overflow: hidden; }
  body { background: var(--page); font-family: "Open Sans", sans-serif; color: var(--text); position: relative; }

  .site-header { height: 90px; background: var(--header); display: flex; align-items: center; padding: 0 150px; position: relative; }
  .brand { display: flex; align-items: center; gap: 10px; color: var(--header-text); font-family: "Oswald", sans-serif; font-size: 18px; letter-spacing: 2px; font-weight: 400; }
  .brand-dot { width: 14px; height: 14px; border-radius: 50%; background: var(--accent); }
  .main-nav { margin-left: auto; display: flex; align-items: center; gap: 6px; }
  .main-nav a { color: var(--header-text); text-decoration: none; font-family: "Oswald", sans-serif; font-size: 14px; letter-spacing: 1px; padding: 8px 14px; position: relative; }
  .main-nav a.is-active { background: var(--accent); color: #fff; }
  .social { display: flex; gap: 8px; margin-left: 14px; }
  .social span { width: 22px; height: 22px; border-radius: 50%; border: 1.5px solid var(--header-text); }

  .dropdown { position: absolute; top: 72px; left: 668px; width: 190px; background: var(--accent); padding: 8px 0; z-index: 5; }
  .dropdown a { display: block; color: #fff; font-size: 12px; padding: 6px 16px; text-decoration: none; border-bottom: 1px solid rgba(255,255,255,0.35); }
  .dropdown a:last-child { border-bottom: none; }

  .title-band { height: 110px; background: var(--band); padding: 26px 150px 0; }
  .breadcrumb { font-size: 11px; color: #9a9090; margin-bottom: 8px; }
  .page-title { font-family: "Oswald", sans-serif; font-weight: 400; font-size: 34px; color: var(--title); letter-spacing: 1px; }

  .content { padding: 36px 150px 0; }
  .post-date { font-size: 12px; font-weight: 600; color: var(--title); margin-bottom: 10px; }
  .post-text { font-size: 13px; line-height: 1.7; max-width: 900px; margin-bottom: 28px; }

  .gallery { display: grid; grid-template-columns: repeat(4, 1fr); grid-template-rows: 250px 250px 200px; gap: 6px; width: 900px; }
  .photo { display: block; }
  .p1 { background: linear-gradient(135deg, #6f9a3e, #b9c96a); }
  .p2 { background: linear-gradient(135deg, #f0b24a, #e6553a); }
  .p3 { background: linear-gradient(135deg, #cfe3ee, #f3d7df); }
  .p4 { background: linear-gradient(135deg, #f4cf4e, #86c2c9); }
  .p5 { background: linear-gradient(135deg, #7a4a3a, #d79a7c); }
  .p6 { background: linear-gradient(135deg, #e9dccb, #c99a5b); }
  .p7 { background: linear-gradient(135deg, #5b3a2f, #d9c19a); }
  .p8 { background: linear-gradient(135deg, #f2c23c, #e58e3c); }
  .p9 { background: linear-gradient(135deg, #3d2f32, #c08a74); }
  .p10 { background: linear-gradient(135deg, #e34f7e, #5aa3d6); }
  .p11 { background: linear-gradient(135deg, #d8b49a, #f1e2d4); }
  .p12 { background: linear-gradient(135deg, #7fa4b6, #e0c6c2); }
</style>
</head>
<body>
  <header class="site-header">
    <div class="brand"><span class="brand-dot"></span>LUME FESTAS</div>
    <nav class="main-nav">
      <a href="#">HOME</a>
      <a href="#">SOBRE NÓS</a>
      <a href="#" class="is-active">GALERIA</a>
      <a href="#">PARCEIROS</a>
      <a href="#">FALE CONOSCO</a>
      <div class="social"><span></span><span></span></div>
    </nav>
    <div class="dropdown">
      <a href="#">Casamentos</a>
      <a href="#">Aniversários</a>
      <a href="#">Festa Infantil</a>
      <a href="#">Eventos Corporativos</a>
    </div>
  </header>

  <section class="title-band">
    <p class="breadcrumb">Início › Galeria › Casamentos</p>
    <h1 class="page-title">CASAMENTO LUÍSA E MARCOS</h1>
  </section>

  <main class="content">
    <p class="post-date">15 de Novembro de 2017</p>
    <p class="post-text">Cada detalhe deste casamento foi pensado junto aos noivos, da paleta de cores às flores escolhidas para a cerimônia ao ar livre. A decoração combinou tons suaves, arranjos delicados e uma mesa de doces cheia de charme, criando um ambiente acolhedor para receber família e amigos em uma noite inesquecível e cheia de alegria.</p>

    <div class="gallery">
      <div class="photo p1" role="img" aria-label="Foto de bandeirinhas de festa sobre fundo verde"></div>
      <div class="photo p2" role="img" aria-label="Foto de copos e chapéus de festa coloridos"></div>
      <div class="photo p3" role="img" aria-label="Foto de mesa de bolo e doces em tons pastel"></div>
      <div class="photo p4" role="img" aria-label="Foto de convidados com decoração colorida ao ar livre"></div>
      <div class="photo p5" role="img" aria-label="Foto de convidados brindando na festa"></div>
      <div class="photo p6" role="img" aria-label="Foto de petiscos servidos em bandeja"></div>
      <div class="photo p7" role="img" aria-label="Foto de taças de espumante alinhadas"></div>
      <div class="photo p8" role="img" aria-label="Foto de decoração com balões amarelos"></div>
      <div class="photo p9" role="img" aria-label="Foto de convidados sorrindo durante a festa"></div>
      <div class="photo p10" role="img" aria-label="Foto de balões coloridos em festa infantil"></div>
      <div class="photo p11" role="img" aria-label="Foto de convidada em momento da celebração"></div>
      <div class="photo p12" role="img" aria-label="Foto de mesa de doces decorada"></div>
    </div>
  </main>
</body>
</html>
```